Rooted Ready Rising: Quiet Roots, Open Doors, Steady Hands

I want a modern and clean looking book cover. 5.25x8

Title
Rooted Ready Rising

Subtitle
Quiet Roots, Open Doors, Steady Hands

I don’t just want a graphic, I want it to make sense. If it can just be the words and a textured looking background, I’ll be ok with that too. I just want it to look crisp, clean, modern.

I want the back to have my book blurb and bio attached with the pic that’s attached.

Target Market(s)

Self help

Requirements
Must have
• Modern, clean look, look professional, attract customers.

```html
<!DOCTYPE html>
<html lang="en">
<head>
<meta charset="utf-8">
<title>Rooted Ready Rising — Book Cover</title>
<link rel="stylesheet" href="https://fonts.googleapis.com/css2?family=Bebas+Neue&family=Montserrat:wght@400;800&display=swap">
<style>
  :root {
    --magenta: #d63a92;
    --magenta-light: #e27ab4;
    --blush: #fbe4ef;
    --plum: #4b0a32;
    --glow: #ffffff;
  }
  html, body {
    margin: 0;
    padding: 0;
    width: 788px;
    height: 1200px;
    overflow: hidden;
    background: var(--magenta);
  }
  .cover {
    position: relative;
    width: 788px;
    height: 1200px;
    overflow: hidden;
    background: var(--magenta);
  }
  .light-burst {
    position: absolute;
    inset: 0;
    background:
      radial-gradient(circle at 100% 0%, rgba(255,255,255,0.95) 0, rgba(255,255,255,0.55) 60px, rgba(240,170,205,0.45) 220px, rgba(226,122,180,0.25) 420px, rgba(214,58,146,0) 640px);
  }
  .title-art {
    position: absolute;
    inset: 0;
  }
  .title-art text {
    font-family: 'Bebas Neue', 'Oswald', sans-serif;
    font-size: 232px;
  }
  .title-light { fill: var(--blush); }
  .title-dark { fill: var(--plum); }
  .subtitle {
    position: absolute;
    left: 440px;
    width: 266px;
    top: 360px;
    margin: 0;
    text-align: center;
    font-family: 'Montserrat', sans-serif;
  }
  .subtitle-line {
    display: block;
    margin-bottom: 62px;
  }
  .subtitle-lead {
    display: block;
    font-weight: 400;
    font-size: 21px;
    letter-spacing: 4px;
    color: var(--plum);
    line-height: 30px;
  }
  .subtitle-key {
    display: block;
    font-weight: 800;
    font-size: 32px;
    letter-spacing: 3px;
    color: var(--blush);
    line-height: 44px;
  }
  .author {
    position: absolute;
    right: 36px;
    bottom: 34px;
    margin: 0;
    font-family: 'Bebas Neue', 'Oswald', sans-serif;
    font-size: 66px;
    letter-spacing: 2px;
    line-height: 1;
    color: var(--blush);
  }
</style>
</head>
<body>
  <main class="cover">
    <div class="light-burst" role="img" aria-label="Soft rays of light streaming from the top right corner"></div>

    <svg class="title-art" width="788" height="1200" viewBox="0 0 788 1200" aria-labelledby="book-title">
      <title id="book-title">Rooted Ready Rising</title>
      <text transform="translate(297,1165) rotate(-90)" x="0" y="0" textLength="1130" lengthAdjust="spacingAndGlyphs"><tspan class="title-light">ROOTED </tspan><tspan class="title-dark">READY </tspan><tspan class="title-light">RISING</tspan></text>
    </svg>

    <h2 class="subtitle">
      <span class="subtitle-line"><span class="subtitle-lead">QUIET</span><span class="subtitle-key">ROOTS,</span></span>
      <span class="subtitle-line"><span class="subtitle-lead">OPEN</span><span class="subtitle-key">DOORS,</span></span>
      <span class="subtitle-line"><span class="subtitle-lead">STEADY</span><span class="subtitle-key">HANDS.</span></span>
    </h2>

    <p class="author">MARISA HOLLOWAY</p>
  </main>
</body>
</html>
```